Lantern Business Cards

Need business cards for my employees at my restaurant.

Needs to include:
Our Logo
Lantern Bowls & Brews
Name: Nora Pettigrew
Title : Owner
Address: 487 Mirella Ave. Lake Havasu City, AZ 86519
Web: www.lanternkestrel.com
Phone: 928-555-0147
Cell: 928-555-0192
Email: info@lanternkestrel.com

```html
<!DOCTYPE html>
<html lang="en">
<head>
<meta charset="utf-8">
<title>Lantern Bowls &amp; Brews – Business Cards</title>
<link rel="stylesheet" href="https://fonts.googleapis.com/css2?family=Roboto:ital,wght@0,300;0,400;0,700;1,400&display=swap">
<style>
  :root {
    --crimson: #a8242f;
    --ink: #0d0d0d;
    --paper: #ffffff;
    --blush: #ecd3d6;
    --rule: #6a6a6a;
    --muted: #d9d9d9;
    --stage: #f2f2f2;
  }
  * { box-sizing: border-box; margin: 0; padding: 0; }
  html, body { width: 813px; height: 1200px; overflow: hidden; }
  body {
    background: var(--stage);
    font-family: "Roboto", Arial, sans-serif;
    position: relative;
  }
  .card {
    position: absolute;
    top: 290px;
    width: 350px;
    height: 620px;
    overflow: hidden;
    box-shadow: 0 6px 18px rgba(0,0,0,0.12);
  }
  /* Back side */
  .card-back {
    left: 36px;
    background: radial-gradient(ellipse at center, var(--paper) 45%, var(--blush) 120%);
  }
  .back-brand {
    position: absolute;
    left: 50%;
    top: 50%;
    transform: translate(-50%, -50%) rotate(-90deg);
    display: flex;
    align-items: center;
    gap: 14px;
    white-space: nowrap;
  }
  .brand-dot {
    width: 22px; height: 22px;
    border-radius: 50%;
    background: var(--crimson);
    flex: none;
  }
  .brand-name {
    color: var(--crimson);
    font-weight: 700;
    text-transform: uppercase;
    letter-spacing: 1px;
    white-space: nowrap;
  }
  .back-brand .brand-name { font-size: 30px; }

  /* Front side */
  .card-front {
    left: 427px;
    background: var(--ink);
  }
  .front-logo {
    height: 272px;
    background: var(--paper);
    display: flex;
    flex-direction: column;
    align-items: center;
    justify-content: center;
    gap: 18px;
    padding: 0 24px;
    text-align: center;
  }
  .front-logo .brand-dot { width: 30px; height: 30px; }
  .front-logo .brand-name { font-size: 22px; }
  .name-band {
    background: var(--crimson);
    height: 78px;
    padding: 12px 0 0 28px;
    color: var(--paper);
  }
  .role { font-style: italic; font-size: 14px; font-weight: 400; }
  .person { font-size: 25px; font-weight: 300; letter-spacing: 0.5px; text-transform: uppercase; margin-top: 2px; }
  .person strong { font-weight: 700; }
  .contacts { padding: 32px 28px 0 28px; color: var(--paper); }
  .contact-row {
    border-bottom: 1px solid var(--rule);
    padding-bottom: 6px;
    margin-bottom: 14px;
    display: flex;
  }
  .contact-row.split { width: 240px; }
  .contact-row.split .field { width: 120px; }
  .field-label { font-size: 14px; display: flex; align-items: center; gap: 6px; }
  .field-label svg { width: 11px; height: 11px; fill: var(--paper); }
  .field-value { font-size: 12px; color: var(--muted); margin-top: 3px; white-space: nowrap; }
</style>
</head>
<body>

<section class="card card-back" aria-label="Card back">
  <div class="back-brand">
    <span class="brand-dot"></span>
    <span class="brand-name">Lantern Bowls &amp; Brews</span>
  </div>
</section>

<section class="card card-front" aria-label="Card front">
  <header class="front-logo">
    <span class="brand-dot"></span>
    <span class="brand-name">Lantern Bowls &amp; Brews</span>
  </header>

  <div class="name-band">
    <p class="role">Owner</p>
    <p class="person"><strong>Nora</strong> Pettigrew</p>
  </div>

  <div class="contacts">
    <div class="contact-row">
      <div class="field">
        <p class="field-label">Addres
          <svg viewBox="0 0 10 10"><path d="M5 0a3.5 3.5 0 0 0-3.5 3.5C1.5 6 5 10 5 10s3.5-4 3.5-6.5A3.5 3.5 0 0 0 5 0zm0 5a1.4 1.4 0 1 1 0-2.8A1.4 1.4 0 0 1 5 5z"/></svg>
        </p>
        <p class="field-value">487 Mirella Ave. Lake Havasu City, AZ 86519</p>
      </div>
    </div>

    <div class="contact-row split">
      <div class="field">
        <p class="field-label">Phone
          <svg viewBox="0 0 10 10"><path d="M2 0l2 2.5-1 1.2a6 6 0 0 0 3.3 3.3l1.2-1L10 8l-1.2 1.7C4.5 10 0 5.5.3 1.2z"/></svg>
        </p>
        <p class="field-value">928-555-0147</p>
      </div>
      <div class="field">
        <p class="field-label">Cell
          <svg viewBox="0 0 10 10"><path d="M3 0h4a1 1 0 0 1 1 1v8a1 1 0 0 1-1 1H3a1 1 0 0 1-1-1V1a1 1 0 0 1 1-1zm0 1.5v6h4v-6z"/></svg>
        </p>
        <p class="field-value">928-555-0192</p>
      </div>
    </div>

    <div class="contact-row split">
      <div class="field">
        <p class="field-label">Website
          <svg viewBox="0 0 10 10"><circle cx="5" cy="5" r="4.4" fill="none" stroke="#fff" stroke-width="1"/><ellipse cx="5" cy="5" rx="1.8" ry="4.4" fill="none" stroke="#fff" stroke-width="0.8"/><path d="M0.6 5h8.8" stroke="#fff" stroke-width="0.8"/></svg>
        </p>
        <p class="field-value">www.lanternkestrel.com</p>
      </div>
    </div>

    <div class="contact-row split">
      <div class="field">
        <p class="field-label">Email
          <svg viewBox="0 0 10 10"><path d="M0 2h10v6H0z"/><path d="M0 2l5 3.5L10 2" fill="none" stroke="#0d0d0d" stroke-width="0.9"/></svg>
        </p>
        <p class="field-value">info@lanternkestrel.com</p>
      </div>
    </div>
  </div>
</section>

</body>
</html>
```